Direct Mail Card for Septic Pumping Company

We need a two-sided, 4x6 direct mailer card for a septic pumping company called Brookhollow Drainage Systems. The card is a coupon for $20 off a free standard septic system pumping, and should entice the card's receivers to call Brookhollow and schedule a pumping prior to December 31.

The card should complement the company website's look and feel (bhdrs.com), and the design should match the holiday-oriented nature of the copy (keep the Christmas feel subtle and elegant).

The attached "wireframes" are not meant to dictate the design, but rather provide inspiration.
Updates

Project Deadline Extended
Reason: Hello all. My client will need a couple more days for final approval, so I am extending the contest until Wednesday. Thanks!

FYI, all:

Thanks to everybody for so many great designs. Tomorrow (Monday) around noon I will be submitting most of these to my client to make a final selection, and there may be a slight modification or two requested to the final selection. I appreciate everybody's participation.

Glen

Thanks to everybody for the great submissions. Our client honestly liked each of them. I appreciate all the effort that went into the project, and hope you will all consider working with us again on future projects.

Regards,

Glen

Target Market(s)

Homeowners whose homes have standard septic systems. Homeowners who know they need their tank pumped, and who are planning to have family over for the holidays.

Industry/Entity Type

It Company

Requirements
Must have
• The copy included in the attached files. A look and feel similar to the company's website (bhdrs.com).

The phone number to use on the card is 830.555.0147

Bleed area needs to be 1/8" on all sides.

```html
<!DOCTYPE html>
<html lang="en">
<head>
<meta charset="utf-8">
<title>Brookhollow Holiday Mailer – Print Layout</title>
<link rel="stylesheet" href="https://fonts.googleapis.com/css2?family=Open+Sans:wght@400;700;800&family=Parisienne&display=swap">
<style>
  :root {
    --sheet: #ffffff;
    --ink: #111111;
    --card-sky: #b8cedb;
    --card-sky-deep: #8fb0c4;
    --panel: rgba(255, 255, 255, 0.72);
    --holiday-red: #d8252c;
    --ribbon-red: #c71f26;
    --navy: #1d3557;
    --band: #8aa6b8;
    --band-dark: #5f7f95;
    --bleed: #111111;
    --trim: #e0467c;
    --safety: #5bb8e8;
    --frame: #bdbdbd;
  }
  * { box-sizing: border-box; margin: 0; padding: 0; }
  html, body { width: 674px; height: 1200px; overflow: hidden; background: var(--sheet); }
  body { position: relative; font-family: "Open Sans", Arial, sans-serif; color: var(--ink); }

  .section-title {
    position: absolute; left: 0; width: 674px; text-align: center;
    font-size: 34px; font-weight: 400; letter-spacing: 0.3px;
  }
  .section-title--printer { top: 8px; }
  .section-title--final { top: 700px; }

  .sheet { position: absolute; left: 45px; width: 595px; height: 440px; }
  .sheet--printer { top: 67px; }
  .sheet--final { top: 760px; border: 1px solid var(--frame); }

  .print-guides { position: absolute; inset: 0; width: 595px; height: 440px; }

  /* Mailer card */
  .card {
    position: absolute; left: 4px; top: 0; width: 315px; height: 432px;
    overflow: hidden;
    background: linear-gradient(160deg, #e9eef1 0%, var(--card-sky) 45%, var(--card-sky-deep) 100%);
  }
  .card__photo {
    position: absolute; inset: 0;
    background: radial-gradient(ellipse at 30% 35%, rgba(255,255,255,0.85) 0%, rgba(230,236,240,0.4) 40%, rgba(120,150,120,0.35) 100%);
  }
  .card__ribbon {
    position: absolute; left: -20px; top: -20px; width: 150px; height: 150px;
    background: radial-gradient(circle at 45% 45%, #e8393f 0%, var(--ribbon-red) 45%, rgba(199,31,38,0) 68%);
    z-index: 1;
  }
  .card__greeting {
    position: absolute; left: 132px; top: 14px; width: 176px; text-align: right;
    font-family: "Parisienne", cursive; font-size: 25px; line-height: 32px; color: var(--holiday-red);
    white-space: nowrap; z-index: 3;
  }
  .card__panel {
    position: absolute; left: 68px; top: 56px; width: 240px; height: 300px;
    background: var(--panel); z-index: 2;
  }
  .card__heading {
    position: absolute; left: 68px; top: 64px; width: 240px; text-align: center;
    font-size: 13.5px; font-weight: 800; line-height: 18px; color: var(--ink);
    font-variant: small-caps; letter-spacing: 0.3px; z-index: 3;
  }
  .card__heading .cap { font-size: 17px; }
  .card__body {
    position: absolute; left: 80px; top: 114px; width: 222px;
    font-size: 12.6px; font-weight: 700; line-height: 16.5px; color: #1a1a1a; z-index: 3;
  }
  .card__body p + p { margin-top: 14px; }
  .card__link { color: var(--holiday-red); }
  .card__band { position: absolute; left: 0; bottom: 0; width: 315px; height: 80px; z-index: 3; }
  .card__brand {
    position: absolute; left: 0; bottom: 8px; width: 160px; height: 50px;
    background: #ffffff; display: flex; align-items: center; gap: 6px; padding-left: 8px;
    font-size: 15px; font-weight: 800; color: var(--navy); z-index: 4;
  }
  .card__brand-mark { width: 12px; height: 12px; background: var(--holiday-red); }
  .card__phone {
    position: absolute; left: 174px; bottom: 20px;
    font-size: 21px; font-weight: 400; color: #ffffff; letter-spacing: 0.5px; z-index: 4;
  }

  .legend { position: absolute; left: 68px; top: 540px; }
  .legend__row { display: flex; align-items: center; height: 33px; }
  .legend__line { width: 120px; height: 0; border-top: 2px solid; margin-right: 34px; }
  .legend__line--bleed { border-color: var(--bleed); }
  .legend__line--trim { border-color: var(--trim); }
  .legend__line--safety { border-color: var(--safety); }
  .legend__label { font-size: 17px; }
</style>
</head>
<body>

<h1 class="section-title section-title--printer">Printer version</h1>

<div class="sheet sheet--printer">
  <div class="card">
    <div class="card__photo" role="img" aria-label="Soft winter photo of a snowy gift scene"></div>
    <div class="card__ribbon" role="img" aria-label="Red satin holiday ribbon and bow"></div>
    <div class="card__greeting">Happy Holidays</div>
    <div class="card__panel"></div>
    <h2 class="card__heading"><span class="cap">H</span>oliday septic<br><span class="cap">S</span>ystem tips</h2>
    <div class="card__body">
      <p>While routine septic pumpings are critical to your system's health, systems overloads during times of heavy usage (like the holidays) can also cause backups - even if your system has been pumped recently.</p>
      <p>Visit <span class="card__link">bhdrs.com/holiday</span> for tips on keeping your septic system running smoothly this holiday season.</p>
    </div>
    <svg class="card__band" viewBox="0 0 315 80" aria-hidden="true">
      <polygon points="0,14 315,0 315,80 0,80" fill="var(--band)"/>
      <polygon points="0,70 315,60 315,80 0,80" fill="var(--band-dark)"/>
    </svg>
    <div class="card__brand"><span class="card__brand-mark"></span>Brookhollow</div>
    <div class="card__phone">830.555.0147</div>
  </div>

  <svg class="print-guides" viewBox="0 0 595 440" aria-hidden="true">
    <rect x="1" y="1" width="593" height="438" fill="none" stroke="var(--bleed)" stroke-width="1.5"/>
    <rect x="8" y="8" width="579" height="424" fill="none" stroke="var(--trim)" stroke-width="1.2"/>
    <rect x="17" y="17" width="561" height="406" fill="none" stroke="var(--safety)" stroke-width="1.2"/>
    <rect x="470" y="8" width="117" height="72" fill="none" stroke="var(--bleed)" stroke-width="1.3" stroke-dasharray="8 6"/>
    <rect x="325" y="135" width="262" height="195" fill="none" stroke="var(--bleed)" stroke-width="1.3" stroke-dasharray="8 6"/>
  </svg>
</div>

<div class="legend">
  <div class="legend__row"><span class="legend__line legend__line--bleed"></span><span class="legend__label">Bleed</span></div>
  <div class="legend__row"><span class="legend__line legend__line--trim"></span><span class="legend__label">Trim Line (where printer will cut)</span></div>
  <div class="legend__row"><span class="legend__line legend__line--safety"></span><span class="legend__label">Safety (no text outside)</span></div>
</div>

<h1 class="section-title section-title--final">Final version</h1>

<div class="sheet sheet--final">
  <div class="card">
    <div class="card__photo" role="img" aria-label="Soft winter photo of a snowy gift scene"></div>
    <div class="card__ribbon" role="img" aria-label="Red satin holiday ribbon and bow"></div>
    <div class="card__greeting">Happy Holidays</div>
    <div class="card__panel"></div>
    <h2 class="card__heading"><span class="cap">H</span>oliday septic<br><span class="cap">S</span>ystem tips</h2>
    <div class="card__body">
      <p>While routine septic pumpings are critical to your system's health, systems overloads during times of heavy usage (like the holidays) can also cause backups - even if your system has been pumped recently.</p>
      <p>Visit <span class="card__link">bhdrs.com/holiday</span> for tips on keeping your septic system running smoothly this holiday season.</p>
    </div>
    <svg class="card__band" viewBox="0 0 315 80" aria-hidden="true">
      <polygon points="0,14 315,0 315,80 0,80" fill="var(--band)"/>
      <polygon points="0,70 315,60 315,80 0,80" fill="var(--band-dark)"/>
    </svg>
    <div class="card__brand"><span class="card__brand-mark"></span>Brookhollow</div>
    <div class="card__phone">830.555.0147</div>
  </div>
</div>

</body>
</html>
```